Car Finance User Dashboard UI Needed

Brisk Motor Lending provides car finance for people in the UK.
We have worked up our design concept but we need it to be much better and have. great mobile option to. as 90% of users come from mobiles.

The job is as follows..
1: Update the UI for all sections of the member dashboard including all pages we need menu options to go direct to each of the example pages as you can see we have not added that yet.

The purpose is to create higher engagement, have more users utilise the car search and make the car search a lot more steamline including the car details page.

2: Rebuild the pages from the ground up to ensure fully mobile friendly and user friendly.
Encourage users to select a car and get a quote.

3: Add to the dashbord page the ability for the user to pick a time a day to arrnge a call back at a time and date they choose.

4: When a user applied to us it takes a few minutes for us to get a responce from a lender so we need a loading bar on the dashboard somewhere to show somthing is happerning we then will provide them with the outcome of the application if it has been accepted or declied. we need to make this very visable but to also allow the user to continue to use the rest of the dashboard.

5 Add option for the user to send. message from the dashbord as well to ask a question.

here is the example

https://www.plandeck.example/file/r7tkLmW2pQ9vxHbNc4TeZY/Brisk-Motor-Lending

Target Market(s)

UK, Car Finance

Industry/Entity Type

Finance

Number of Pages Required

5+ page

Font styles to use
Other font styles liked:
• use the same as our site

Requirements
Must have
• Colour palet should match my main website and fonts should be simple and clean use fonts syle from main website https://www.briskmotorlending.example.co.uk/

```html
<!DOCTYPE html>
<html lang="en">
<head>
<meta charset="utf-8">
<meta name="viewport" content="width=device-width, initial-scale=1">
<title>Brisk Motor Lending – Member Dashboard</title>
<link href="https://fonts.googleapis.com/css2?family=Open+Sans:wght@400;600;700&family=Roboto+Condensed:wght@400;700&display=swap" rel="stylesheet">
<style>
:root{
  --topbar:#f3f3f3;
  --nav:#6b6b6b;
  --nav-active:#4b4b4b;
  --panel:#f2f2f2;
  --ink:#333333;
  --muted:#8a8a8a;
  --line:#9a9a9a;
  --field-border:#d6d6d6;
  --photo:#8e8e8e;
  --btn:#666666;
  --btn-light:#9b9b9b;
  --progress-track:#dcdcdc;
  --progress-fill:#555555;
  --white:#ffffff;
}
*{box-sizing:border-box;margin:0;padding:0}
html,body{width:827px;height:1200px;overflow:hidden;background:var(--white)}
body{font-family:"Open Sans",Arial,sans-serif;color:var(--ink);position:relative}
.wrap{position:absolute;left:138px;width:550px}

.topbar{position:absolute;top:0;left:0;width:827px;height:26px;background:var(--topbar);border-bottom:1px solid #e2e2e2;font-size:7.5px;color:var(--muted)}
.topbar .contact{position:absolute;left:138px;top:8px}
.topbar .contact span+span{margin-left:11px}
.topbar .counters{position:absolute;right:139px;top:5px;display:flex;align-items:center;gap:8px}
.counter{position:relative;width:15px;height:15px;border-radius:50%;background:#e1e1e1;display:flex;align-items:center;justify-content:center}
.counter b{position:absolute;top:-4px;right:-5px;width:9px;height:9px;border-radius:50%;background:#a9a9a9;color:#fff;font-size:5.5px;font-weight:600;display:flex;align-items:center;justify-content:center}

.header{position:absolute;top:26px;left:0;width:827px;height:61px}
.brand{position:absolute;left:153px;top:22px;display:flex;align-items:center;gap:6px;font-size:14px;font-weight:600;color:#555}
.brand i{display:block;width:14px;height:14px;border-radius:50%;background:#555}
.logout{position:absolute;left:620px;top:21px;width:68px;height:19px;background:var(--btn);color:#fff;border-radius:2px;font-size:8.5px;display:flex;align-items:center;justify-content:center;gap:6px}

.nav{position:absolute;top:87px;left:0;width:827px;height:27px;background:var(--nav)}
.nav a{position:absolute;top:0;height:27px;display:flex;align-items:center;gap:5px;color:#fff;font-size:9px;text-decoration:none}
.nav a.active{background:var(--nav-active);left:134px;width:87px;justify-content:center}

/* application status */
.app-status{position:absolute;left:138px;top:119px;width:550px;height:20px;background:var(--panel);border-left:3px solid var(--progress-fill);display:flex;align-items:center;gap:8px;padding:0 8px;font-size:7px;color:#555}
.app-status strong{font-weight:600;color:#333}
.progress{flex:1;height:5px;background:var(--progress-track);border-radius:3px;overflow:hidden}
.progress span{display:block;width:62%;height:100%;background:var(--progress-fill)}
.app-status .note{color:var(--muted)}

.section-title{font-family:"Roboto Condensed",Arial,sans-serif;font-weight:400;font-size:16.5px;color:#555;border-bottom:1px solid var(--line);padding-bottom:3px}

.search-panel{position:absolute;left:138px;top:187px;width:550px;height:155px;background:var(--panel)}
.field-label{position:absolute;font-size:7.5px;color:var(--ink)}
.field{position:absolute;height:19px;background:#fff;border:1px solid var(--field-border);font-size:8px;color:#555;padding-left:5px;display:flex;align-items:center}
.field.select svg{position:absolute;right:6px;top:6px}
.field.disabled{background:#f4f4f4}
.map-pin{position:absolute;left:82px;top:27px;width:10px;height:10px;border-radius:50%;background:#777;display:flex;align-items:center;justify-content:center}
.tooltip{position:absolute;left:79px;top:6px;width:62px;height:14px;background:#fff;border-radius:2px;box-shadow:0 0 3px rgba(0,0,0,.15);font-size:6.5px;color:#666;display:flex;align-items:center;justify-content:center}
.advanced{position:absolute;left:430px;top:130px;font-size:8px;color:#666}
.search-btn{position:absolute;left:494px;top:127px;width:43px;height:16px;background:var(--btn);color:#fff;border-radius:2px;font-size:8px;display:flex;align-items:center;justify-content:center}

/* call back + message */
.contact-tools{position:absolute;left:138px;top:349px;width:550px;display:grid;grid-template-columns:1fr 1fr;gap:10px}
.tool{height:30px;background:var(--panel);display:flex;align-items:center;gap:5px;padding:0 7px;font-size:7px}
.tool-title{font-weight:600;color:#333;white-space:nowrap}
.mini-field{height:17px;background:#fff;border:1px solid var(--field-border);font-size:7px;color:var(--muted);padding:0 4px;display:flex;align-items:center}
.mini-btn{height:17px;padding:0 8px;background:var(--btn);color:#fff;border-radius:2px;font-size:7px;display:flex;align-items:center}

.cars{position:absolute;left:138px;top:427px;width:550px;display:grid;grid-template-columns:repeat(3,149px);column-gap:51px;row-gap:45px}
.car{height:212px}
.car-photo{position:relative;width:149px;height:94px;background:var(--photo)}
.badge{position:absolute;left:-1px;top:9px;width:41px;height:16px;background:#6f6f6f;color:#fff;font-family:"Roboto Condensed",Arial,sans-serif;font-size:7px;display:flex;align-items:center;justify-content:center;border-radius:2px}
.video{position:absolute;right:8px;bottom:8px;width:14px;height:14px;background:#6a6a6a;display:flex;align-items:center;justify-content:center}
.car-title{font-family:"Roboto Condensed",Arial,sans-serif;font-weight:400;font-size:11px;margin-top:7px;color:#333}
.price{display:inline-block;font-family:"Roboto Condensed",Arial,sans-serif;font-weight:700;font-size:11.5px;color:#666;border-bottom:1px dashed #888;line-height:13px;margin-top:1px}
.specs{list-style:none;margin-top:4px;font-size:8px;line-height:13px;color:var(--muted)}
.specs b{color:#222;font-weight:600}
.details{display:inline-flex;margin-top:8px;width:36px;height:16px;background:var(--btn-light);color:#fff;font-size:7.5px;align-items:center;justify-content:center;border-radius:1px}

.to-top{position:absolute;left:742px;top:1151px;width:36px;height:35px;background:#777;display:flex;align-items:center;justify-content:center}

/* small screens */
@media (max-width:600px){
  html,body{width:100%;height:auto;overflow:auto}
  .topbar .contact{display:none}
  .nav{overflow-x:auto}
  .wrap,.app-status,.search-panel,.contact-tools,.cars{position:static;width:auto;margin:10px}
  .contact-tools{grid-template-columns:1fr}
  .cars{grid-template-columns:1fr}
  .car-photo{width:100%}
}
</style>
</head>
<body>
<div class="topbar">
  <div class="contact"><span>48 Ardley Row, Leeds, LS2 7QX</span><span>+44 113 496 0720</span></div>
  <div class="counters">
    <span>Compare</span>
    <span class="counter"><svg width="9" height="8" viewBox="0 0 9 8" fill="none" stroke="#777" stroke-width=".8"><path d="M4.5 0.5v7M1 7.5h7M1.5 2h6M1.5 2L0.5 4.5h2zM7.5 2L6.5 4.5h2z"/></svg><b>0</b></span>
    <span style="margin-left:4px">Wishlist</span>
    <span class="counter"><svg width="8" height="7" viewBox="0 0 8 7"><path d="M4 7L.6 3.6A1.8 1.8 0 0 1 4 1.2a1.8 1.8 0 0 1 3.4 2.4z" fill="#777"/></svg><b>0</b></span>
  </div>
</div>

<header class="header">
  <div class="brand"><i></i>Brisk Motor Lending</div>
  <div class="logout"><svg width="9" height="8" viewBox="0 0 9 8" fill="none" stroke="#fff" stroke-width=".9"><path d="M3.5 1H1v6h2.5M3 4h5.5M6.5 2l2 2-2 2"/></svg>Logout</div>
</header>

<nav class="nav">
  <a class="active"><svg width="9" height="9" viewBox="0 0 9 9" fill="none" stroke="#fff" stroke-width="1"><circle cx="3.8" cy="3.8" r="3"/><path d="M6 6l2.5 2.5"/></svg>Search</a>
  <a style="left:262px"><svg width="9" height="8" viewBox="0 0 9 8" fill="none" stroke="#fff" stroke-width=".9"><path d="M4.5 7.3L1 3.8A2 2 0 0 1 4.5 1.3a2 2 0 0 1 3.5 2.5z"/></svg>Wishlist</a>
  <a style="left:373px"><svg width="10" height="9" viewBox="0 0 10 9" fill="none" stroke="#fff" stroke-width=".8"><path d="M5 .5v8M1.5 8.5h7M1.5 2h7M1.5 2L.5 5h2zM8.5 2L7.5 5h2z"/></svg>Compare</a>
  <a style="left:490px"><svg width="8" height="9" viewBox="0 0 8 9" fill="none" stroke="#fff" stroke-width=".8"><rect x=".5" y=".5" width="7" height="8"/><path d="M2 2.5h4M2 4.5h1M4 4.5h1M2 6.5h1M4 6.5h1"/></svg>Loan Calculator</a>
  <a style="left:632px"><svg width="7" height="9" viewBox="0 0 7 9" fill="none" stroke="#fff" stroke-width=".8"><path d="M.5.5h4l2 2v6h-6z"/></svg>Paperwork</a>
</nav>

<div class="app-status" role="status">
  <strong>Application in progress</strong>
  <span>Checking with lenders…</span>
  <div class="progress"><span></span></div>
  <span class="note">Keep browsing – we'll show your result here</span>
</div>

<h2 class="section-title wrap" style="top:148px">Car Search</h2>

<form class="search-panel">
  <span class="field-label" style="left:12px;top:12px">Location</span>
  <div class="tooltip">Select from map</div>
  <div class="field select" style="left:12px;top:23px;width:66px">City<svg width="7" height="5" viewBox="0 0 7 5" fill="none" stroke="#444" stroke-width=".9"><path d="M.5.8l3 3 3-3"/></svg></div>
  <span class="map-pin"><svg width="6" height="6" viewBox="0 0 6 6" fill="none" stroke="#fff" stroke-width=".8"><circle cx="3" cy="3" r="1.8"/></svg></span>
  <div class="field select" style="left:101px;top:23px;width:82px"><svg width="7" height="5" viewBox="0 0 7 5" fill="none" stroke="#444" stroke-width=".9"><path d="M.5.8l3 3 3-3"/></svg></div>
  <span class="field-label" style="left:189px;top:12px">Condition:</span>
  <div class="field select" style="left:189px;top:23px;width:171px"><svg width="7" height="5" viewBox="0 0 7 5" fill="none" stroke="#444" stroke-width=".9"><path d="M.5.8l3 3 3-3"/></svg></div>
  <span class="field-label" style="left:367px;top:12px">Make:</span>
  <div class="field" style="left:367px;top:23px;width:82px">Any</div>
  <span class="field-label" style="left:455px;top:12px">Model:</span>
  <div class="field select disabled" style="left:455px;top:23px;width:83px"><svg width="7" height="5" viewBox="0 0 7 5" fill="none" stroke="#bbb" stroke-width=".9"><path d="M.5.8l3 3 3-3"/></svg></div>

  <span class="field-label" style="left:12px;top:50px">Price (€) min/max</span>
  <div class="field" style="left:12px;top:62px;width:83px"></div>
  <div class="field select" style="left:101px;top:62px;width:82px"><svg width="7" height="5" viewBox="0 0 7 5" fill="none" stroke="#444" stroke-width=".9"><path d="M.5.8l3 3 3-3"/></svg></div>
  <span class="field-label" style="left:189px;top:50px">Year</span>
  <div class="field" style="left:189px;top:62px;width:83px">min</div>
  <div class="field" style="left:278px;top:62px;width:83px">max</div>
  <span class="field-label" style="left:367px;top:50px">Kilometer min/max</span>
  <div class="field" style="left:367px;top:62px;width:82px"></div>
  <div class="field" style="left:455px;top:62px;width:83px"></div>

  <span class="field-label" style="left:12px;top:89px">Fuel Type</span>
  <span class="field-label" style="left:101px;top:89px">Gearbox</span>
  <span class="field-label" style="left:189px;top:89px">Body Type</span>
  <span class="field-label" style="left:278px;top:89px">Door Count</span>
  <span class="field-label" style="left:367px;top:89px">Color</span>
  <div class="field select" style="left:12px;top:100px;width:83px"><svg width="7" height="5" viewBox="0 0 7 5" fill="none" stroke="#444" stroke-width=".9"><path d="M.5.8l3 3 3-3"/></svg></div>
  <div class="field select" style="left:101px;top:100px;width:82px"><svg width="7" height="5" viewBox="0 0 7 5" fill="none" stroke="#444" stroke-width=".9"><path d="M.5.8l3 3 3-3"/></svg></div>
  <div class="field select" style="left:189px;top:100px;width:83px"><svg width="7" height="5" viewBox="0 0 7 5" fill="none" stroke="#444" stroke-width=".9"><path d="M.5.8l3 3 3-3"/></svg></div>
  <div class="field select" style="left:278px;top:100px;width:83px"><svg width="7" height="5" viewBox="0 0 7 5" fill="none" stroke="#444" stroke-width=".9"><path d="M.5.8l3 3 3-3"/></svg></div>
  <div class="field select" style="left:367px;top:100px;width:82px"><svg width="7" height="5" viewBox="0 0 7 5" fill="none" stroke="#444" stroke-width=".9"><path d="M.5.8l3 3 3-3"/></svg></div>
  <div class="field select" style="left:455px;top:100px;width:83px"><svg width="7" height="5" viewBox="0 0 7 5" fill="none" stroke="#444" stroke-width=".9"><path d="M.5.8l3 3 3-3"/></svg></div>

  <span class="advanced">[+] Advanced</span>
  <span class="search-btn">Search</span>
</form>

<section class="contact-tools">
  <div class="tool callback">
    <span class="tool-title">Arrange a call back</span>
    <span class="mini-field" style="width:62px">Pick a date</span>
    <span class="mini-field" style="width:50px">Time</span>
    <span class="mini-btn">Book</span>
  </div>
  <div class="tool message">
    <span class="tool-title">Ask us a question</span>
    <span class="mini-field" style="flex:1">Type your message…</span>
    <span class="mini-btn">Send</span>
  </div>
</section>

<h2 class="section-title wrap" style="top:388px">Recent Cars</h2>

<section class="cars">
  <article class="car"><div class="car-photo" role="img" aria-label="Photo of a sedan for sale"><span class="badge">FEATURED</span><span class="video"><svg width="8" height="6" viewBox="0 0 8 6"><rect width="5" height="6" fill="#fff"/><path d="M5 3l3-2.5v5z" fill="#fff"/></svg></span></div><h3 class="car-title">Do cillum Lorem cillum. Veniam</h3><span class="price">€150.000</span><ul class="specs"><li><b>Location:</b> Ipsum / aliqua / adipisicing</li><li><b>Engine:</b> 6.5 cm³ LP, Petrol</li><li><b>Kilometer:</b> 30000 km</li><li><b>Condition:</b> used</li></ul><span class="details">Details</span></article>
  <article class="car"><div class="car-photo" role="img" aria-label="Photo of a sedan for sale"><span class="badge">FEATURED</span><span class="video"><svg width="8" height="6" viewBox="0 0 8 6"><rect width="5" height="6" fill="#fff"/><path d="M5 3l3-2.5v5z" fill="#fff"/></svg></span></div><h3 class="car-title">Do cillum Lorem cillum. Veniam</h3><span class="price">€150.000</span><ul class="specs"><li><b>Location:</b> Ipsum / aliqua / adipisicing</li><li><b>Engine:</b> 6.5 cm³ LP, Petrol</li><li><b>Kilometer:</b> 30000 km</li><li><b>Condition:</b> used</li></ul><span class="details">Details</span></article>
  <article class="car"><div class="car-photo" role="img" aria-label="Photo of a sedan for sale"><span class="badge">FEATURED</span><span class="video"><svg width="8" height="6" viewBox="0 0 8 6"><rect width="5" height="6" fill="#fff"/><path d="M5 3l3-2.5v5z" fill="#fff"/></svg></span></div><h3 class="car-title">Do cillum Lorem cillum. Veniam</h3><span class="price">€150.000</span><ul class="specs"><li><b>Location:</b> Ipsum / aliqua / adipisicing</li><li><b>Engine:</b> 6.5 cm³ LP, Petrol</li><li><b>Kilometer:</b> 30000 km</li><li><b>Condition:</b> used</li></ul><span class="details">Details</span></article>
  <article class="car"><div class="car-photo" role="img" aria-label="Photo of a sedan for sale"><span class="badge">FEATURED</span><span class="video"><svg width="8" height="6" viewBox="0 0 8 6"><rect width="5" height="6" fill="#fff"/><path d="M5 3l3-2.5v5z" fill="#fff"/></svg></span></div><h3 class="car-title">Do cillum Lorem cillum. Veniam</h3><span class="price">€150.000</span><ul class="specs"><li><b>Location:</b> Ipsum / aliqua / adipisicing</li><li><b>Engine:</b> 6.5 cm³ LP, Petrol</li><li><b>Kilometer:</b> 30000 km</li><li><b>Condition:</b> used</li></ul><span class="details">Details</span></article>
  <article class="car"><div class="car-photo" role="img" aria-label="Photo of a sedan for sale"><span class="badge">FEATURED</span><span class="video"><svg width="8" height="6" viewBox="0 0 8 6"><rect width="5" height="6" fill="#fff"/><path d="M5 3l3-2.5v5z" fill="#fff"/></svg></span></div><h3 class="car-title">Do cillum Lorem cillum. Veniam</h3><span class="price">€150.000</span><ul class="specs"><li><b>Location:</b> Ipsum / aliqua / adipisicing</li><li><b>Engine:</b> 6.5 cm³ LP, Petrol</li><li><b>Kilometer:</b> 30000 km</li><li><b>Condition:</b> used</li></ul><span class="details">Details</span></article>
  <article class="car"><div class="car-photo" role="img" aria-label="Photo of a sedan for sale"><span class="badge">FEATURED</span><span class="video"><svg width="8" height="6" viewBox="0 0 8 6"><rect width="5" height="6" fill="#fff"/><path d="M5 3l3-2.5v5z" fill="#fff"/></svg></span></div><h3 class="car-title">Do cillum Lorem cillum. Veniam</h3><span class="price">€150.000</span><ul class="specs"><li><b>Location:</b> Ipsum / aliqua / adipisicing</li><li><b>Engine:</b> 6.5 cm³ LP, Petrol</li><li><b>Kilometer:</b> 30000 km</li><li><b>Condition:</b> used</li></ul><span class="details">Details</span></article>
  <article class="car"><div class="car-photo" role="img" aria-label="Photo of a sedan for sale"><span class="badge">FEATURED</span><span class="video"><svg width="8" height="6" viewBox="0 0 8 6"><rect width="5" height="6" fill="#fff"/><path d="M5 3l3-2.5v5z" fill="#fff"/></svg></span></div><h3 class="car-title">Do cillum Lorem cillum. Veniam</h3><span class="price">€150.000</span><ul class="specs"><li><b>Location:</b> Ipsum / aliqua / adipisicing</li><li><b>Engine:</b> 6.5 cm³ LP, Petrol</li><li><b>Kilometer:</b> 30000 km</li><li><b>Condition:</b> used</li></ul><span class="details">Details</span></article>
  <article class="car"><div class="car-photo" role="img" aria-label="Photo of a sedan for sale"><span class="badge">FEATURED</span><span class="video"><svg width="8" height="6" viewBox="0 0 8 6"><rect width="5" height="6" fill="#fff"/><path d="M5 3l3-2.5v5z" fill="#fff"/></svg></span></div><h3 class="car-title">Do cillum Lorem cillum. Veniam</h3><span class="price">€150.000</span><ul class="specs"><li><b>Location:</b> Ipsum / aliqua / adipisicing</li><li><b>Engine:</b> 6.5 cm³ LP, Petrol</li><li><b>Kilometer:</b> 30000 km</li><li><b>Condition:</b> used</li></ul><span class="details">Details</span></article>
  <article class="car"><div class="car-photo" role="img" aria-label="Photo of a sedan for sale"><span class="badge">FEATURED</span><span class="video"><svg width="8" height="6" viewBox="0 0 8 6"><rect width="5" height="6" fill="#fff"/><path d="M5 3l3-2.5v5z" fill="#fff"/></svg></span></div><h3 class="car-title">Do cillum Lorem cillum. Veniam</h3><span class="price">€150.000</span><ul class="specs"><li><b>Location:</b> Ipsum / aliqua / adipisicing</li><li><b>Engine:</b> 6.5 cm³ LP, Petrol</li><li><b>Kilometer:</b> 30000 km</li><li><b>Condition:</b> used</li></ul><span class="details">Details</span></article>
</section>

<a class="to-top" aria-label="Back to top"><svg width="11" height="12" viewBox="0 0 11 12" fill="none" stroke="#fff" stroke-width="1.3"><path d="M5.5 11.5V1M1 5.5l4.5-4.5L10 5.5"/></svg></a>
</body>
</html>
```